Qamra
قمرة كافيه
Hello Designers:-
Please check your e-mail inbox.
Thank you so much!
plz star rating...
The front and the back of the card should be one color "Beige". In front, it only shows the logo, the address, e-mail, twitter and instagram accounts. No need to type any other word like the word "قمرة"
As for the back, we want a loyalty card with 6 stamps with "Qamra" shape drawing on each. and the 6th qamra has a FREE written on it (Pic provided in brief)
If you have any comments, questions or requirements please do not hesitate to contact me on my e-mail or here, in the discussion.
Thank you so much for your work! :)
Hello designers: Please make sure to read the project brief as we want a (Double) sided business card/loyalty card. Moreover, please be aware that the card color should follow the color of the store "Beige" and not the logo color (Store pic provided in the brief)
Thank you so much for your effort! And good luck!

```html
<!DOCTYPE html>
<html lang="en">
<head>
<meta charset="utf-8">
<title>Qamra – Business &amp; Loyalty Card</title>
<link href="https://fonts.googleapis.com/css2?family=Amiri:wght@400;700&family=Arimo:wght@400;700&display=swap" rel="stylesheet">
<style>
  :root {
    --backdrop: #d9d7d3;
    --border-brown: #4d2622;
    --beige-light: #d8bc92;
    --beige-dark: #bf9c6c;
    --frame-cream: #efdcbc;
    --ink-brown: #4a2a1c;
    --logo-cream: #f7ecd9;
  }
  * { margin: 0; padding: 0; box-sizing: border-box; }
  html, body { width: 1200px; height: 901px; overflow: hidden; }
  body {
    background: var(--backdrop);
    display: flex;
    align-items: center;
    justify-content: center;
    gap: 40px;
    font-family: "Arimo", Arial, sans-serif;
  }
  .card {
    position: relative;
    width: 540px;
    height: 310px;
    background: var(--border-brown);
    padding: 13px;
    box-shadow: 0 6px 18px rgba(0,0,0,.18);
  }
  .card-face {
    position: relative;
    width: 100%;
    height: 100%;
    background: radial-gradient(ellipse at 50% 40%, var(--beige-light), var(--beige-dark));
  }
  .card-frame {
    position: absolute;
    inset: 0;
    width: 100%;
    height: 100%;
  }
  .card-frame rect, .card-frame path { fill: none; stroke: var(--frame-cream); stroke-width: 1.4; }

  /* Loyalty side */
  .loyalty {
    position: absolute;
    inset: 0;
    display: flex;
    flex-direction: column;
    align-items: center;
    justify-content: center;
  }
  .brand-name {
    font-family: "Amiri", serif;
    font-weight: 700;
    font-size: 52px;
    line-height: 1.1;
    color: var(--logo-cream);
  }
  .loyalty-offer {
    margin-top: 8px;
    font-size: 14px;
    color: var(--ink-brown);
  }
  .stamp-row {
    list-style: none;
    display: flex;
    gap: 16px;
    margin-top: 20px;
  }
  .stamp {
    width: 46px;
    height: 46px;
    border-radius: 50%;
    border: 1.5px solid var(--frame-cream);
    background: rgba(247, 236, 217, .18);
    display: flex;
    align-items: center;
    justify-content: center;
  }
  .stamp-free {
    background: var(--border-brown);
    border-color: var(--border-brown);
    color: var(--logo-cream);
    font-size: 11px;
    font-weight: 700;
    letter-spacing: .5px;
  }

  /* Contact side */
  .contact {
    position: absolute;
    top: 0;
    bottom: 0;
    right: 46px;
    left: 46px;
    display: flex;
    align-items: center;
    justify-content: flex-end;
    color: var(--ink-brown);
  }
  .contact-list { list-style: none; }
  .contact-list li {
    display: flex;
    justify-content: flex-end;
    align-items: center;
    gap: 8px;
    font-size: 13px;
    line-height: 1.2;
    margin-bottom: 10px;
  }
  .contact-list li:last-child { margin-bottom: 0; }
  .contact-list .address { font-family: "Amiri", serif; font-size: 15px; }
  .address-text { direction: rtl; }
  .contact-icon { width: 13px; height: 13px; flex: none; }
  .contact-icon * { fill: var(--ink-brown); }
  .social-dot { width: 11px; height: 11px; border-radius: 50%; background: var(--ink-brown); flex: none; }
  .follow-label { margin-top: 18px; }
</style>
</head>
<body>

  <!-- Contact side -->
  <section class="card card-contact" aria-label="Card front">
    <div class="card-face">
      <svg class="card-frame" viewBox="0 0 514 284" preserveAspectRatio="none" aria-hidden="true">
        <path d="M30 14 H484 V30 H500 V254 H484 V270 H30 V254 H14 V30 H30 Z"/>
        <rect x="14" y="14" width="16" height="16"/>
        <rect x="484" y="14" width="16" height="16"/>
        <rect x="14" y="254" width="16" height="16"/>
        <rect x="484" y="254" width="16" height="16"/>
      </svg>
      <div class="contact">
        <ul class="contact-list">
          <li class="address"><span class="address-text">منطقة الشويخ الصناعية، الشارع الأول</span>
            <svg class="contact-icon" viewBox="0 0 12 12"><path d="M6 0a4 4 0 0 0-4 4c0 3 4 8 4 8s4-5 4-8a4 4 0 0 0-4-4zm0 5.5A1.5 1.5 0 1 1 6 2.5a1.5 1.5 0 0 1 0 3z"/></svg>
          </li>
          <li>55501234
            <svg class="contact-icon" viewBox="0 0 12 12"><path d="M2.5 0.5l2 2.2-1 1.5c.7 1.6 2 2.9 3.6 3.6l1.5-1 2.2 2-1.3 2.2C5 11 1 7 .3 1.8z"/></svg>
          </li>
          <li>QamraKuwait@mailbox.kw
            <svg class="contact-icon" viewBox="0 0 12 12"><path d="M0 2h12v8H0zM1 3l5 3.5L11 3v-.2H1z" fill-rule="evenodd"/></svg>
          </li>
          <li class="follow-label">Follow us on</li>
          <li>@Qamra <span class="social-dot"></span></li>
          <li>@QamraKuwait <span class="social-dot"></span></li>
        </ul>
      </div>
    </div>
  </section>

  <!-- Loyalty side -->
  <section class="card card-loyalty" aria-label="Card back">
    <div class="card-face">
      <svg class="card-frame" viewBox="0 0 514 284" preserveAspectRatio="none" aria-hidden="true">
        <path d="M30 14 H484 V30 H500 V254 H484 V270 H30 V254 H14 V30 H30 Z"/>
        <rect x="14" y="14" width="16" height="16"/>
        <rect x="484" y="14" width="16" height="16"/>
        <rect x="14" y="254" width="16" height="16"/>
        <rect x="484" y="254" width="16" height="16"/>
      </svg>
      <div class="loyalty">
        <p class="brand-name">قمرة</p>
        <p class="loyalty-offer">Buy 5 and get the 6th refill for free</p>
        <ol class="stamp-row" aria-label="Loyalty stamps">
          <li class="stamp" aria-label="Stamp 1"></li>
          <li class="stamp" aria-label="Stamp 2"></li>
          <li class="stamp" aria-label="Stamp 3"></li>
          <li class="stamp" aria-label="Stamp 4"></li>
          <li class="stamp" aria-label="Stamp 5"></li>
          <li class="stamp stamp-free">FREE</li>
        </ol>
      </div>
    </div>
  </section>

</body>
</html>
```